themed infographic with multiple stats/charts

**Requires previous infographic experience and examples.**We need a skilled illustrator/designer to take an organized list of stats we've gathered related to the topic of investing and turn them into a professional looking, long, infographic with multiple sections, with a clear visual theme.We are not looking to match our branding guidelines. This will have a style and look all its own, with a goal of being compelling and sharable.Stats/content provided when we engage.

Target Market(s)

US customers, 25-45 years old

Colors

Designer to choose colors to be used in the design.

Requirements
Must have
• interesting theme that ties all the stats together, but separate panels for each stat
Should not have
• will not accept something that looks like cheap clip art

```html
<!DOCTYPE html>
<html lang="en">
<head>
<meta charset="utf-8">
<title>Investing in Your 20's, 30's, 40's, 50's and 60's</title>
<link rel="stylesheet" href="https://fonts.googleapis.com/css2?family=Oswald:wght@500;600;700&family=Roboto:wght@500;700&display=swap">
<style>
  :root {
    --navy: #1b3f78;
    --green: #46b64a;
    --ink: #555a5f;
    --icon-ink: #3c4750;
    --white: #ffffff;
  }
  * { margin: 0; padding: 0; box-sizing: border-box; }
  html, body { width: 1200px; height: 3178px; overflow: hidden; background: var(--white); }
  .canvas { position: relative; width: 1200px; height: 3178px; overflow: hidden; font-family: "Roboto", Arial, sans-serif; color: var(--ink); }
  .abs { position: absolute; }
  .bands { position: absolute; inset: 0; }

  .display {
    font-family: "Oswald", "Arial Narrow", sans-serif;
    font-weight: 700;
    line-height: 1;
    white-space: nowrap;
    transform: scaleX(var(--sx, 1));
    transform-origin: left top;
  }
  .centered { left: 0; width: 1200px; text-align: center; transform-origin: center top; }

  .title-top { top: 82px; font-size: 148px; color: var(--navy); --sx: 0.92; }
  .title-ages { top: 226px; font-size: 104px; color: var(--green); --sx: 0.83; }

  .section-head { font-size: 52px; font-weight: 600; color: var(--navy); left: 48px; --sx: 0.88; }
  .section-head.light { color: var(--white); }
  .rule { height: 3px; background: var(--navy); left: 0; }
  .rule.light { background: var(--white); }

  .body { font-size: 31px; font-weight: 500; line-height: 1; color: var(--ink); white-space: nowrap; }
  .body.white { color: var(--white); }
  .body.bold { font-weight: 700; }
  .body.green { color: var(--green); }

  .big-green { color: var(--green); }
  .big-white { color: var(--white); }
  .stat-60s p { font-size: 27px; line-height: 36.6px; }
</style>
</head>
<body>
<div class="canvas">

  <svg class="bands" width="1200" height="3178" viewBox="0 0 1200 3178">
    <defs>
      <linearGradient id="teal-grad" x1="0" y1="0" x2="1" y2="1">
        <stop offset="0" stop-color="#135a6b"/>
        <stop offset="1" stop-color="#0b3845"/>
      </linearGradient>
      <linearGradient id="green-grad" x1="0" y1="0" x2="1" y2="0">
        <stop offset="0" stop-color="#28a02f"/>
        <stop offset="0.5" stop-color="#3aa83c"/>
        <stop offset="1" stop-color="#1c8a24"/>
      </linearGradient>
      <linearGradient id="navy-grad" x1="0" y1="0" x2="0" y2="1">
        <stop offset="0" stop-color="#1c4386"/>
        <stop offset="1" stop-color="#112b5d"/>
      </linearGradient>
      <linearGradient id="photo-soft" x1="0" y1="0" x2="1" y2="0">
        <stop offset="0" stop-color="#ffffff" stop-opacity="0"/>
        <stop offset="0.55" stop-color="#dfe6e8" stop-opacity="0.55"/>
        <stop offset="1" stop-color="#eef2f3" stop-opacity="0.2"/>
      </linearGradient>
    </defs>
    <rect x="0" y="440" width="1200" height="360" fill="url(#photo-soft)" role="img" aria-label="Photo of a young professional saving money at a desk"/>
    <polygon points="0,795 1200,684 1200,1270 0,1196" fill="url(#teal-grad)" role="img" aria-label="Photo of a young professional at a desk, tinted teal"/>
    <polygon points="0,1782 1200,1677 1200,2177 0,2097" fill="url(#green-grad)" role="img" aria-label="Photo of banknotes, tinted green"/>
    <polygon points="0,2701 1200,2590 1200,3178 0,3178" fill="url(#navy-grad)" role="img" aria-label="Photo of a financial planning desk, tinted blue"/>

    <g fill="none" stroke="#ffffff" stroke-width="6" stroke-linejoin="round" stroke-linecap="round">
      <polyline points="822,845 880,800 905,815 958,768"/>
      <polygon points="958,758 972,760 966,774" fill="#fff"/>
      <rect x="826" y="878" width="22" height="32"/>
      <rect x="858" y="858" width="22" height="52"/>
      <rect x="890" y="838" width="22" height="72"/>
      <rect x="922" y="808" width="22" height="102"/>
      <line x1="814" y1="912" x2="978" y2="912"/>
    </g>

    <g fill="none" stroke="#ffffff" stroke-width="5" stroke-linecap="round" stroke-linejoin="round">
      <circle cx="604" cy="1860" r="26"/>
      <text x="604" y="1872" text-anchor="middle" font-family="Roboto, sans-serif" font-size="34" font-weight="700" fill="#fff" stroke="none">$</text>
      <path d="M566,1890 C556,1910 560,1935 580,1952"/>
      <path d="M642,1890 C652,1910 648,1935 628,1952"/>
    </g>

    <g fill="none" stroke="#3c4750" stroke-width="7" stroke-linecap="round" stroke-linejoin="round">
      <circle cx="880" cy="2275" r="62"/>
      <polyline points="808,2292 842,2240 880,2268 918,2222 952,2212"/>
      <circle cx="808" cy="2292" r="7" fill="#fff"/>
      <circle cx="842" cy="2240" r="7" fill="#fff"/>
      <circle cx="880" cy="2268" r="7" fill="#fff"/>
      <circle cx="918" cy="2222" r="7" fill="#fff"/>
      <circle cx="952" cy="2212" r="7" fill="#fff"/>
      <line x1="880" y1="2337" x2="880" y2="2355"/>
      <polyline points="812,2355 948,2355"/>
      <line x1="812" y1="2355" x2="812" y2="2368"/>
      <line x1="948" y1="2355" x2="948" y2="2368"/>
      <line x1="880" y1="2355" x2="880" y2="2368"/>
      <circle cx="812" cy="2390" r="22"/>
      <circle cx="880" cy="2390" r="22"/>
      <circle cx="948" cy="2390" r="22"/>
      <line x1="937" y1="2390" x2="959" y2="2390"/>
      <line x1="948" y1="2379" x2="948" y2="2401"/>
      <circle cx="880" cy="2390" r="8"/>
    </g>
    <text x="812" y="2400" text-anchor="middle" font-family="Roboto, sans-serif" font-size="26" font-weight="700" fill="#3c4750">$</text>
  </svg>

  <h1 class="abs display centered title-top">INVESTING IN YOUR</h1>
  <div class="abs display centered title-ages">20'S, 30'S, 40'S, 50'S AND 60'S</div>

  <!-- 20s -->
  <h2 class="abs display section-head" style="top:372px;">INVESTING IN YOUR 20'S</h2>
  <div class="abs rule" style="top:430px;width:582px;"></div>
  <p class="abs body" style="left:52px;top:468px;">Start saving</p>
  <p class="abs body" style="left:52px;top:516px;">Start first retirement account</p>
  <div class="abs display big-green" style="left:50px;top:556px;font-size:142px;--sx:0.9;">15%</div>
  <div class="abs body" style="left:297px;top:566px;line-height:41px;">Set aside 15%<br>of income in<br>retirement account</div>
  <p class="abs body" style="left:684px;top:468px;">Learn compound interest</p>
  <div class="abs body" style="left:684px;top:521px;line-height:48px;">Understand matching 401(k) -<br>average 401k employer<br>contributions growing</div>

  <!-- 30s -->
  <h2 class="abs display section-head light" style="top:877px;">INVESTING IN YOUR 30'S</h2>
  <div class="abs rule light" style="top:936px;width:549px;"></div>
  <p class="abs body white" style="left:48px;top:958px;">Build emergency fund of 3-6 months</p>
  <p class="abs body white" style="left:48px;top:994px;">worth of expenses</p>
  <p class="abs body white" style="left:48px;top:1036px;">Increase retirement contributions</p>
  <p class="abs body white" style="left:48px;top:1078px;">Have equivalent of annual salary saved by age 30</p>
  <div class="abs display big-green" style="left:664px;top:920px;font-size:138px;--sx:0.9;">2x</div>
  <div class="abs body bold green" style="left:808px;top:926px;line-height:40px;">Have twice annual<br>salary saved by age 35</div>
  <div class="abs body bold white" style="left:808px;top:1010px;font-size:24px;line-height:36px;">Increase finance knowledge -<br>Understand difference between<br>various investment funds<br>(mutual fund, etf, index)</div>

  <!-- 40s -->
  <h2 class="abs display section-head" style="top:1326px;">INVESTING IN YOUR 40'S</h2>
  <div class="abs rule" style="top:1388px;width:582px;"></div>
  <p class="abs body" style="left:46px;top:1424px;">Diversify investments</p>
  <p class="abs body" style="left:46px;top:1473px;">Keep investment fees low</p>
  <p class="abs body" style="left:46px;top:1521px;">Reduce or eliminate debt</p>
  <p class="abs body" style="left:46px;top:1570px;">Have 3x your annual salary saved</p>
  <p class="abs body" style="left:46px;top:1612px;">by 40 and 4x by 45</p>
  <div class="abs display" style="left:623px;top:1318px;font-size:72px;color:var(--navy);--sx:0.88;"><span class="big-green">63,000</span> saved in 40's</div>
  <p class="abs body" style="left:626px;top:1416px;">Average american has 4k in liquid</p>
  <p class="abs body" style="left:626px;top:1458px;">savings and 63k in retirement funds</p>
  <div class="abs display big-green" style="left:625px;top:1514px;font-size:42px;font-weight:600;--sx:0.85;">250,000? IS WHAT SHOULD BE SAVED</div>
  <p class="abs body" style="left:629px;top:1573px;font-size:29px;">Use HSA or FSA accounts</p>
  <p class="abs body" style="left:629px;top:1615px;font-size:29px;">Life insurance bought and understood</p>

  <!-- 50s -->
  <h2 class="abs display section-head light" style="top:1845px;">INVESTING IN YOUR 50'S</h2>
  <div class="abs rule light" style="top:1905px;width:477px;"></div>
  <p class="abs body bold white" style="left:48px;top:1930px;font-size:27px;">Avoid new debt</p>
  <p class="abs body bold white" style="left:48px;top:1970px;font-size:27px;">Take advantage of retirement catch-ups</p>
  <p class="abs body bold white" style="left:48px;top:2009px;font-size:27px;">(differences between 401k, IRAs, and HSA)</p>
  <div class="abs display" style="left:667px;top:1830px;font-size:76px;color:var(--white);--sx:0.83;">6x-8x Salary Saved</div>
  <p class="abs body bold white" style="left:670px;top:1918px;font-size:32px;">Have 6x-8x annual salary saved</p>
  <p class="abs body bold white" style="left:670px;top:1958px;font-size:32px;">by retirement</p>
  <p class="abs body bold white" style="left:670px;top:2008px;font-size:24px;">Dont remove investments from stocks too</p>
  <p class="abs body bold white" style="left:670px;top:2044px;font-size:24px;">much, but diversify further</p>

  <!-- 60s -->
  <h2 class="abs display section-head" style="top:2210px;">INVESTING IN YOUR 60'S</h2>
  <div class="abs rule" style="top:2270px;width:582px;"></div>
  <div class="abs display big-green" style="left:46px;top:2296px;font-size:138px;--sx:0.86;">10x</div>
  <p class="abs body" style="left:222px;top:2308px;">Stay the course - Have 8x</p>
  <p class="abs body" style="left:222px;top:2345px;">annual salary by 60 and</p>
  <p class="abs body" style="left:222px;top:2381px;">10x by 67</p>
  <div class="abs stat-60s" style="left:52px;top:2431px;">
    <p class="body">Average american has 8k in liquid savings and median retirement account value of 172k</p>
    <p class="body">Average social security benefit is only 1.4k (Need more SSA info Dana)</p>
    <p class="body">Understand required minimum distribution (RMD) - differences between 401k and IRAs</p>
    <p class="body">Life expectancy and preparing for that</p>
    <p class="body">May need to work longer</p>
    <p class="body">Downsize</p>
  </div>

  <!-- Overall -->
  <h2 class="abs display" style="left:113px;top:2752px;font-size:84px;font-weight:600;color:var(--white);--sx:0.85;">OVERALL INVESTING INFORMATION</h2>
  <div class="abs display big-green" style="left:118px;top:2860px;font-size:128px;--sx:0.87;">56%</div>
  <div class="abs display big-white" style="left:645px;top:2860px;font-size:128px;--sx:0.87;">35%</div>
  <div class="abs body bold white" style="left:113px;top:2982px;font-size:29px;line-height:39.5px;">of households currently have money<br>in an employer-sponsored retirement<br>account (including pensions,<br>401(k)s, and others).</div>
  <div class="abs body bold white" style="left:641px;top:2982px;font-size:29px;line-height:39.5px;">Americans don’t participate in any<br>retirement savings plan at all.</div>

</div>
</body>
</html>
```